Bussines Card - TR EDIFICACIONES, S.A.

We need a design for a business card.
I want it to look professional, but not old fashion.
We are like "young people', somehow i want it to look fresh, new, different, but still serious and professional.
I could use, a non typical design. (I mean, not just rectangular design).

The company Name is " TR EDIFICACIONES, S.A. " we are Panamenian company (spanish language) dedicated to construction and civil engeniering.

The company logo is attached, i use it with white background. Im not sure trying different one, could try.

Industry/Entity Type

Business

```html
<!DOCTYPE html>
<html lang="es">
<head>
<meta charset="utf-8">
<title>TR Edificaciones – Tarjeta de presentación</title>
<link rel="stylesheet" href="https://fonts.googleapis.com/css2?family=Fira+Sans+Condensed:wght@600&family=Open+Sans:wght@400;600&display=swap">
<style>
  :root {
    --backdrop: #e6e4e0;
    --card-light: #ffffff;
    --card-dark: #58585c;
    --ink-grey: #58585c;
    --ink-white: #ffffff;
  }
  * { margin: 0; padding: 0; box-sizing: border-box; }
  html, body {
    width: 1200px;
    height: 1000px;
    overflow: hidden;
    background: var(--backdrop);
  }
  .canvas {
    position: relative;
    width: 1200px;
    height: 1000px;
  }
  .card {
    position: absolute;
    top: 162px;
    width: 430px;
    height: 718px;
    border-radius: 30px;
  }
  .card-front { left: 146px; background: var(--card-light); }
  .card-back  { left: 580px; background: var(--card-dark); }

  .brand-square {
    position: absolute;
    left: 144px;
    top: 69px;
    width: 148px;
    height: 147px;
    background: var(--ink-grey);
  }
  .brand-name {
    position: absolute;
    left: 0;
    width: 100%;
    top: 245px;
    text-align: center;
    font-family: "Fira Sans Condensed", "Arial Narrow", sans-serif;
    font-weight: 600;
    font-size: 28px;
    letter-spacing: 4px;
    color: var(--ink-grey);
  }
  .address {
    position: absolute;
    left: 64px;
    top: 618px;
    font-family: "Open Sans", Arial, sans-serif;
    font-size: 21px;
    line-height: 30px;
    color: var(--ink-grey);
  }
  .address .pin {
    display: inline-block;
    width: 14px;
    height: 20px;
    margin-right: 4px;
    vertical-align: -2px;
  }

  .holder {
    position: absolute;
    right: 37px;
    top: 128px;
    text-align: right;
    font-family: "Open Sans", Arial, sans-serif;
    font-size: 29px;
    line-height: 40px;
    color: var(--ink-white);
  }
  .holder-name { font-weight: 600; }
  .holder-title { font-weight: 400; }

  .contact-list {
    position: absolute;
    right: 37px;
    top: 592px;
    list-style: none;
    text-align: right;
    font-family: "Open Sans", Arial, sans-serif;
    font-size: 21px;
    line-height: 30px;
    color: var(--ink-white);
  }
  .contact-list li { display: flex; justify-content: flex-end; align-items: center; }
  .contact-list svg { width: 19px; height: 19px; margin-left: 9px; }
</style>
</head>
<body>
<main class="canvas">
  <section class="card card-front">
    <div class="brand-square"></div>
    <div class="brand-name">TR EDIFICACIONES</div>
    <p class="address">
      <svg class="pin" viewBox="0 0 14 20" aria-hidden="true"><path d="M7 0C3.1 0 0 3.1 0 7c0 5 7 13 7 13s7-8 7-13C14 3.1 10.9 0 7 0z" fill="var(--ink-grey)"/><circle cx="7" cy="7" r="2.6" fill="var(--card-light)"/></svg>Calle 48, Bella Vista,<br>Plaza Norte, 2do Piso Local 4
    </p>
  </section>

  <section class="card card-back">
    <div class="holder">
      <div class="holder-name">YOUR NAME HERE</div>
      <div class="holder-title">YOUR TITLE</div>
    </div>
    <ul class="contact-list">
      <li>281-5037
        <svg viewBox="0 0 20 20" aria-hidden="true"><circle cx="10" cy="10" r="10" fill="var(--ink-white)"/><path d="M6.2 4.8l2 2.2-1 1.4c.8 1.7 2 2.9 3.7 3.7l1.4-1 2.2 2-1.2 1.6c-4-.7-7.2-3.9-7.9-7.9z" fill="var(--card-dark)"/></svg>
      </li>
      <li>12345678910
        <svg viewBox="0 0 20 20" aria-hidden="true"><circle cx="10" cy="10" r="10" fill="var(--ink-white)"/><rect x="6.5" y="4" width="7" height="12" rx="1.2" fill="var(--card-dark)"/><rect x="7.7" y="5.5" width="4.6" height="7" fill="var(--ink-white)"/></svg>
      </li>
      <li>Youremailadd@here.com
        <svg viewBox="0 0 20 20" aria-hidden="true"><circle cx="10" cy="10" r="10" fill="var(--ink-white)"/><rect x="5" y="6.5" width="10" height="7" rx="1" fill="var(--card-dark)"/><path d="M5.5 7l4.5 3.4L14.5 7" stroke="var(--ink-white)" stroke-width="1.1" fill="none"/></svg>
      </li>
    </ul>
  </section>
</main>
</body>
</html>
```